Endocrinologist needs new stationery

I have a logo from ArtHiveLab and now need stationery with the new logo.

Address: Suite 4, 238 Kestrel Lane, Richmond, VIC 3121
Phone: 03 9412 7053
Fax: 03 9412 7055
Website: www.drmelvaparkson.com.au
Email: admin@drmelvaparkson.com.au

```html
<!DOCTYPE html>
<html lang="en">
<head>
<meta charset="utf-8">
<title>Dr Melva Parkson – Stationery</title>
<link href="https://fonts.googleapis.com/css2?family=Montserrat:wght@300;400;500&display=swap" rel="stylesheet">
<style>
:root{
  --bg:#5b5b5d;
  --paper:#ffffff;
  --blue:#5b8fc2;
  --mauve:#9c8495;
  --plum:#6f5672;
  --ink:#4a4a52;
  --muted:#8a8a92;
}
*{box-sizing:border-box;margin:0;padding:0}
html,body{width:1200px;height:1200px;overflow:hidden}
body{background:var(--bg);font-family:"Montserrat",sans-serif;color:var(--ink);position:relative}
.sheet{position:absolute;background:var(--paper);overflow:hidden}
.wave{position:absolute;left:0;bottom:0;width:100%}
.brand-name{font-family:"Montserrat",sans-serif;font-weight:300;color:var(--blue);letter-spacing:.5px;white-space:nowrap}

/* Letterhead */
.letterhead{left:60px;top:220px;width:500px;height:720px}
.letterhead .brand-name{position:absolute;left:40px;top:64px;font-size:24px}
.letterhead .address{position:absolute;left:40px;top:100px;font-size:8.5px;color:var(--muted)}
.contact-list{position:absolute;right:34px;top:34px;list-style:none;font-size:8px;color:var(--muted)}
.contact-list li{display:flex;align-items:center;gap:6px;margin-bottom:4px}
.contact-list .dot{width:7px;height:7px;background:var(--mauve);border-radius:1px}
.letter-body{position:absolute;left:40px;top:140px;width:420px;font-size:8.5px;line-height:1.6;color:var(--ink)}
.letter-body p{margin-bottom:11px}
.letter-body .date{margin-bottom:8px}
.signature{width:120px;height:30px;margin-top:6px;background:linear-gradient(90deg,rgba(156,132,149,.35),rgba(156,132,149,.1));border-radius:4px}

/* Compliments slip */
.slip{left:620px;top:220px;width:520px;height:250px}
.slip .brand-name{position:absolute;left:40px;top:58px;font-size:24px}
.slip .address{position:absolute;left:36px;bottom:20px;font-size:8.5px;color:#fff;z-index:2}

/* Envelope */
.envelope{left:620px;top:500px;width:520px;height:260px}
.envelope .flap{position:absolute;left:0;top:0;width:100%;height:100%}

/* Business cards */
.card{top:800px;width:250px;height:146px}
.card-front{left:620px}
.card-front .details{position:absolute;right:14px;top:12px;list-style:none;font-size:6px;color:var(--muted);line-height:1.5}
.card-front .details .dot{display:inline-block;width:5px;height:5px;background:var(--mauve);margin-right:4px}
.card-front .brand-name{position:absolute;left:16px;top:76px;font-size:13px}
.card-back{left:890px;background:var(--mauve)}
.card-back .brand-name{position:absolute;left:0;right:0;top:44px;text-align:center;font-size:16px;color:#fff}
</style>
</head>
<body>

<section class="sheet letterhead">
  <div class="brand-name">Dr Melva Parkson</div>
  <div class="address">Suite 4, 238 Kestrel Lane, Richmond, VIC 3121</div>
  <ul class="contact-list">
    <li><span class="dot"></span>03 9412 7053</li>
    <li><span class="dot"></span>03 9412 7055</li>
    <li><span class="dot"></span>www.drmelvaparkson.com.au</li>
    <li><span class="dot"></span>admin@drmelvaparkson.com.au</li>
  </ul>
  <div class="letter-body">
    <p class="date">May 03, 2025</p>
    <p>To the Former Company name,</p>
    <p>Lorem ipsum is simply dummy text of the printing and typesetting industry. Lorem ipsum has been the industry's standard dummy text ever since the 1500s, when an unknown printer took a galley of type and scrambled it to make a type specimen book.</p>
    <p>It has survived not only five centuries, but also the leap into electronic typesetting, remaining essentially unchanged. It was popularised in the 1960s with the release of sheets containing passages.</p>
    <p>Lorem ipsum is simply dummy text of the printing and typesetting industry. Lorem ipsum has been the industry's standard dummy text ever since the 1500s, when an unknown printer took a galley of type and scrambled it to make a type specimen book.</p>
    <p>Sincerely yours,</p>
    <div class="signature" role="img" aria-label="Handwritten signature of Dr Melva Parkson"></div>
  </div>
  <svg class="wave" viewBox="0 0 500 130" height="130" aria-hidden="true">
    <path d="M0 130 L0 92 C160 70 330 55 500 0 L500 130 Z" fill="var(--blue)"/>
    <path d="M0 80 C170 62 340 42 500 -6" fill="none" stroke="var(--plum)" stroke-width="3"/>
  </svg>
</section>

<section class="sheet slip">
  <div class="brand-name">Dr Melva Parkson</div>
  <svg class="wave" viewBox="0 0 520 170" height="170" aria-hidden="true">
    <path d="M0 170 L0 120 C180 110 380 80 520 0 L520 170 Z" fill="var(--blue)"/>
    <path d="M0 106 C190 96 390 62 520 -12" fill="none" stroke="var(--plum)" stroke-width="3"/>
  </svg>
  <div class="address">Suite 4, 238 Kestrel Lane, Richmond, VIC 3121</div>
</section>

<section class="sheet envelope">
  <svg class="flap" viewBox="0 0 520 260" aria-hidden="true">
    <path d="M0 0 H520 V40 L490 70 H30 L0 40 Z" fill="var(--blue)"/>
  </svg>
</section>

<section class="sheet card card-front">
  <ul class="details">
    <li>Suite 4, 238 Kestrel Lane</li>
    <li>Richmond, VIC 3121</li>
    <li><span class="dot"></span>03 9412 7053</li>
    <li><span class="dot"></span>03 9412 7055</li>
    <li><span class="dot"></span>www.drmelvaparkson.com.au</li>
    <li><span class="dot"></span>admin@drmelvaparkson.com.au</li>
  </ul>
  <div class="brand-name">Dr Melva Parkson</div>
  <svg class="wave" viewBox="0 0 250 60" height="60" aria-hidden="true">
    <path d="M0 60 L0 46 C90 40 180 26 250 0 L250 60 Z" fill="var(--blue)"/>
    <path d="M0 38 C90 32 180 18 250 -6" fill="none" stroke="var(--plum)" stroke-width="2"/>
  </svg>
</section>

<section class="sheet card card-back">
  <div class="brand-name">Dr Melva Parkson</div>
  <svg class="wave" viewBox="0 0 250 60" height="60" aria-hidden="true">
    <path d="M0 60 L0 46 C90 40 180 26 250 0 L250 60 Z" fill="#ffffff"/>
    <path d="M0 38 C90 32 180 18 250 -6" fill="none" stroke="var(--plum)" stroke-width="2"/>
  </svg>
</section>

</body>
</html>
```